Business cards and logo for kitchen and bath remodeling company

We want an elegant card but that calls attention something unique and when people see it they remember us. A log that we can use for our own. We are a kitchen and bathroom remodeling company. We are 3 partners staring the company we are located in seattle washington usa. We try to give the best experience and luxury look in our projects and we are looking to show that in our cards. I added a sample of a card I really like. I like the black and gold look but gray blue or green in a metallic look would look nice. I'm open to any color.

Target Market(s)

Home owners.

Industry/Entity Type

Construction

Contact Information for Business Card

Larchmont and Vey builders

Colors

Designer to choose colors to be used in the design.

Requirements
Must have
• Make a Logo
• Logo to be unique
• Name of company larchmont and vey builders
Nice to have
• Have a good color scheme
• Front design to connect with back of card

```html
<!DOCTYPE html>
<html lang="en">
<head>
<meta charset="utf-8">
<title>Larchmont and Vey Builders – Business Card</title>
<link rel="stylesheet" href="https://fonts.googleapis.com/css2?family=Lato:wght@400;700&display=swap">
<style>
  :root {
    --backdrop: #5e5e5e;
    --card: #050505;
    --gold: #c98a26;
    --gold-light: #d9a441;
    --ink-light: #f2f2f2;
    --ink-faint: #2c2c2c;
  }
  * { box-sizing: border-box; margin: 0; padding: 0; }
  html, body {
    width: 1200px; height: 900px; overflow: hidden;
    background: var(--backdrop);
    font-family: "Lato", sans-serif;
  }
  .stage { position: relative; width: 1200px; height: 900px; }
  .card {
    position: absolute;
    width: 540px; height: 308px;
    background: var(--card);
    border: 2px solid var(--gold);
    box-shadow: 0 14px 30px rgba(0,0,0,.45);
  }
  .card--back { left: 600px; top: 120px; }
  .card--front { left: 70px; top: 470px; }

  .brand { display: flex; align-items: center; gap: 14px; }
  .brand__square { width: 46px; height: 46px; border: 2px solid currentColor; flex: none; }
  .brand__name { font-weight: 400; line-height: 1.15; }

  .card--back .brand {
    position: absolute; left: 50%; top: 50%;
    transform: translate(-50%, -50%);
    color: var(--ink-faint);
  }
  .card--back .brand__square { width: 60px; height: 60px; }
  .card--back .brand__name { font-size: 30px; }

  .card--front .brand {
    position: absolute; left: 34px; top: 118px;
    color: var(--gold-light);
  }
  .card--front .brand__name { font-size: 19px; }

  .divider {
    position: absolute; left: 262px; top: 96px;
    width: 2px; height: 116px; background: var(--gold);
  }
  .contact { position: absolute; left: 292px; top: 92px; }
  .contact__name { color: var(--gold); font-weight: 700; font-size: 25px; }
  .contact__role { color: var(--ink-light); font-size: 14px; margin: 4px 0 14px; }
  .contact__list { list-style: none; }
  .contact__item {
    display: flex; align-items: center; gap: 10px;
    color: var(--ink-light); font-size: 14px; margin-bottom: 6px;
  }
  .contact__icon { width: 13px; height: 13px; flex: none; }
</style>
</head>
<body>
<main class="stage">
  <section class="card card--back" aria-label="Card back">
    <div class="brand">
      <span class="brand__square"></span>
      <span class="brand__name">Larchmont and Vey Builders</span>
    </div>
  </section>

  <section class="card card--front" aria-label="Card front">
    <div class="brand">
      <span class="brand__square"></span>
      <span class="brand__name">Larchmont and Vey<br>Builders</span>
    </div>
    <span class="divider"></span>
    <div class="contact">
      <p class="contact__name">Marisol Edevane</p>
      <p class="contact__role">Founder &amp; CEO</p>
      <ul class="contact__list">
        <li class="contact__item">
          <svg class="contact__icon" viewBox="0 0 16 16"><path d="M3 1l3 3-2 2c1 2 3 4 5 5l2-2 3 3-2 3C6 14 2 10 1 3z" fill="var(--gold)"/></svg>
          206 5550147
        </li>
        <li class="contact__item">
          <svg class="contact__icon" viewBox="0 0 16 16"><rect x="1" y="3" width="14" height="10" fill="var(--gold)"/><path d="M1 3l7 6 7-6" fill="none" stroke="var(--card)" stroke-width="1.4"/></svg>
          hello@larchmontvey.com
        </li>
        <li class="contact__item">
          <svg class="contact__icon" viewBox="0 0 16 16"><circle cx="8" cy="8" r="7" fill="var(--gold)"/><path d="M1 8h14M8 1c-3 4-3 10 0 14M8 1c3 4 3 10 0 14" fill="none" stroke="var(--card)" stroke-width="1"/></svg>
          www.larchmontvey.com
        </li>
      </ul>
    </div>
  </section>
</main>
</body>
</html>
```